会社のロゴを新しくしましたので、名刺のデザインを募集いたします。
記載項目
●名刺
表面
会社名・部署名・役職・氏名・携帯電話・住所・TEL・FAX・mail・URL
裏面
ロゴをいれてデザインしてください。

データをご納品いただければ、印刷はこちらで行います。
Adobe Creative Cloudで、Adobe fontsを使用しておりますので、そちらで
対応可能なフォントで作成をお願いします。
ロゴデータが複数色ありますが、どの色を使用するかはお任せします。

丸みを帯びたデザインで、シンプルに地球を表現しており
飽きが来なさそうでいいと思いました。

多数の素敵なデザインを提案いただきありがとうございます。 また何かございましたら、よろしくお願いいたします。

```html
<!DOCTYPE html>
<html lang="ja">
<head>
<meta charset="utf-8">
<title>ノヴァ株式会社 名刺デザイン</title>
<link href="https://fonts.googleapis.com/css2?family=Noto+Sans+JP:wght@300;400;500;700&display=swap" rel="stylesheet">
<style>
  :root {
    --stage: #e9eaea;
    --paper: #ffffff;
    --teal: #2a9ea3;
    --ink: #2f3438;
    --ink-soft: #555b60;
    --card-shadow: rgba(0,0,0,0.12);
  }
  * { margin: 0; padding: 0; box-sizing: border-box; }
  html, body { width: 849px; height: 1200px; overflow: hidden; }
  body {
    background: var(--stage);
    font-family: "Noto Sans JP", sans-serif;
    color: var(--ink);
    position: relative;
  }
  .card {
    position: absolute;
    left: 79px;
    width: 691px;
    height: 408px;
    box-shadow: 0 1px 4px var(--card-shadow);
  }
  .card--front { top: 249px; background: var(--paper); }
  .card--back { top: 696px; background: var(--teal); }

  .front__brand {
    position: absolute;
    left: 40px; top: 160px;
    width: 250px;
    text-align: center;
    font-size: 66px;
    font-weight: 500;
    letter-spacing: 1px;
    color: var(--ink);
    line-height: 1;
  }
  .front__rule {
    position: absolute;
    left: 269px; top: 20px;
    width: 3px; height: 354px;
    background: var(--teal);
  }
  .front__info { position: absolute; left: 292px; top: 80px; }
  .company { font-size: 24px; font-weight: 500; line-height: 1; }
  .company .dept { font-size: 14px; font-weight: 400; margin-left: 10px; }
  .person { margin-top: 20px; padding-left: 40px; }
  .person__title { font-size: 11px; color: var(--ink-soft); }
  .person__name { font-size: 32px; font-weight: 400; line-height: 1.15; letter-spacing: 2px; }
  .person__roman { font-size: 12px; color: var(--ink-soft); }
  .contacts { margin-top: 20px; list-style: none; }
  .contacts li {
    display: flex; align-items: center;
    font-size: 14px; height: 23px; color: var(--ink);
  }
  .contacts .pair { margin-left: 28px; display: flex; align-items: center; }
  .icon { width: 13px; height: 13px; margin-right: 7px; fill: var(--teal); flex: none; }

  .back__brand {
    position: absolute; left: 0; right: 0; top: 125px;
    text-align: center;
    font-size: 74px; font-weight: 500; line-height: 1;
    color: var(--paper);
  }
  .back__tagline {
    position: absolute; left: 0; right: 0; top: 221px;
    text-align: center;
    font-size: 12px; font-weight: 300; letter-spacing: 0.5px;
    color: var(--paper);
    padding-left: 0;
  }
</style>
</head>
<body>
  <svg width="0" height="0" style="position:absolute" aria-hidden="true">
    <symbol id="i-phone" viewBox="0 0 16 16"><path d="M4 1l3 3-2 2c1 2 3 4 5 5l2-2 3 3-2 3C7 15 1 9 1 3z"/></symbol>
    <symbol id="i-fax" viewBox="0 0 16 16"><rect x="1" y="6" width="14" height="8" rx="2"/><rect x="4" y="1" width="8" height="6"/></symbol>
    <symbol id="i-pin" viewBox="0 0 16 16"><path d="M8 0a5.5 5.5 0 0 0-5.5 5.5C2.5 10 8 16 8 16s5.5-6 5.5-10.5A5.5 5.5 0 0 0 8 0zm0 8a2.5 2.5 0 1 1 0-5 2.5 2.5 0 0 1 0 5z"/></symbol>
    <symbol id="i-mail" viewBox="0 0 16 16"><path d="M1 3h14v10H1z M1 3l7 6 7-6" stroke="#fff" stroke-width="1.2"/></symbol>
    <symbol id="i-home" viewBox="0 0 16 16"><path d="M8 1l7 7h-2v7H3V8H1z"/></symbol>
  </svg>

  <section class="card card--front">
    <div class="front__brand">nova</div>
    <div class="front__rule"></div>
    <div class="front__info">
      <p class="company">ノヴァ株式会社<span class="dept">営業本部</span></p>
      <div class="person">
        <p class="person__title">代表取締役</p>
        <p class="person__name">山田 太郎</p>
        <p class="person__roman">Taro Yamada</p>
      </div>
      <ul class="contacts">
        <li><svg class="icon"><use href="#i-phone"/></svg>000-0000-0000<span class="pair"><svg class="icon"><use href="#i-fax"/></svg>0000-00-0000</span></li>
        <li><svg class="icon"><use href="#i-pin"/></svg>〒000-0000 ○○県○○市○○○1-1-1</li>
        <li><svg class="icon"><use href="#i-mail"/></svg>○○○○@○○○○○○.co.jp</li>
        <li><svg class="icon"><use href="#i-home"/></svg>https://www.○○○○○.com</li>
      </ul>
    </div>
  </section>

  <section class="card card--back">
    <div class="back__brand">nova</div>
    <p class="back__tagline">Nova Integrated Technologists</p>
  </section>
</body>
</html>
```